Business card

We need a business card design for our company based in Auckland , New Zealand called 'Kestrel + Design Ltd'. We provide architectural services. We would like to see designs that use the max. three colours (such as white, black, grey) The final design should communicate financial safety and growth."
Also I will provide our company logo. I would like to the logo to be embeded onto our business card.

Target Market(s)

new residential house, alteration & addition & light commericila design & drafting service

Industry/Entity Type

Architecture

Contact Information for Business Card

Company name: kestrel + design Ltd.
Name: Mark Telford
Job title: architectural designer & Design RQC
email address: mark@kdstudio.co.nz
mobile number: 02 5319 6620
web site: www.kdstudio.co.nz

Requirements
Must have
• My project must have..
• - embeded logo (attached company logo)
• I don't have a bigger version for our company logo, but I have one old one, so you can remove the word from it)
• - insert the attached small PDGQ logo & RQC logo
• - creative, simple and clear business card.
• - Max. three colours
Nice to have
• - Here are the samples I would like to share with you: http://www.velmorindex.com/blog/minimalistic-business-card-designs/
• I would like to have my business card like one of the creation.
Should not have
• TBA

```html
<!DOCTYPE html>
<html lang="en">
<head>
<meta charset="utf-8">
<title>Kestrel + Design Ltd — Business Card</title>
<link rel="stylesheet" href="https://fonts.googleapis.com/css2?family=Fjalla+One&family=Raleway:ital,wght@0,300;0,400;0,700;1,400&display=swap">
<style>
  :root {
    --page: #e4e4e4;
    --ink-black: #050507;
    --glow-navy: #1d2160;
    --panel-grey: #3d3d3f;
    --paper-white: #ffffff;
    --soft-grey: #d4d4d4;
    --badge-grey: #8a8a8a;
  }
  html, body {
    margin: 0;
    padding: 0;
    width: 1200px;
    height: 900px;
    overflow: hidden;
    background: var(--page);
  }
  .canvas {
    position: relative;
    width: 1200px;
    height: 900px;
  }
  .card {
    position: absolute;
    left: 250px;
    width: 700px;
    height: 400px;
    overflow: hidden;
    box-shadow: 0 10px 28px rgba(0,0,0,0.25);
  }
  /* Front face */
  .card-front {
    top: 30px;
    background: radial-gradient(ellipse 62% 55% at 50% 38%, var(--glow-navy) 0%, #0d0f2c 45%, var(--ink-black) 80%);
  }
  .front-brand {
    position: absolute;
    left: 0;
    right: 0;
    top: 178px;
    display: flex;
    justify-content: center;
    align-items: center;
    gap: 14px;
  }
  .brand-dot {
    width: 16px;
    height: 16px;
    border-radius: 50%;
    background: var(--paper-white);
  }
  .brand-name {
    font-family: "Fjalla One", sans-serif;
    font-size: 32px;
    color: var(--paper-white);
    letter-spacing: 0.5px;
  }
  /* Back face */
  .card-back {
    top: 470px;
    background: var(--paper-white);
  }
  .back-panel {
    position: absolute;
    left: 0;
    top: 0;
    width: 354px;
    height: 100%;
    background: var(--panel-grey);
  }
  .holder-name {
    position: absolute;
    left: 40px;
    top: 52px;
    margin: 0;
    font-family: "Raleway", sans-serif;
    font-size: 30px;
    font-weight: 300;
    color: var(--paper-white);
    letter-spacing: 0.5px;
  }
  .holder-name strong { font-weight: 700; }
  .holder-title {
    position: absolute;
    left: 40px;
    top: 92px;
    margin: 0;
    font-family: "Raleway", sans-serif;
    font-style: italic;
    font-size: 15px;
    color: var(--soft-grey);
  }
  .contact-box {
    position: absolute;
    left: 10px;
    top: 138px;
    width: 393px;
    height: 179px;
    box-sizing: border-box;
    border: 5px solid var(--paper-white);
    border-radius: 26px;
    background: var(--panel-grey);
  }
  .contact-list {
    list-style: none;
    margin: 0;
    padding: 0;
    position: absolute;
    right: 80px;
    top: 30px;
  }
  .contact-item {
    display: flex;
    justify-content: flex-end;
    align-items: center;
    gap: 12px;
    height: 40px;
    font-family: "Raleway", sans-serif;
    font-size: 19px;
    color: var(--soft-grey);
  }
  .contact-icon {
    position: absolute;
    right: -44px;
    width: 28px;
    height: 28px;
  }
  .contact-item { position: relative; }
  .badge-seal {
    position: absolute;
    left: 465px;
    top: 54px;
    width: 96px;
    height: 96px;
    border-radius: 50%;
    background: var(--panel-grey);
  }
  .badge-member {
    position: absolute;
    left: 482px;
    top: 185px;
    width: 80px;
    height: 62px;
    border-radius: 6px;
    background: var(--badge-grey);
  }
</style>
</head>
<body>
<main class="canvas">
  <section class="card card-front" aria-label="Card front">
    <div class="front-brand">
      <span class="brand-dot"></span>
      <span class="brand-name">kestrel + design Ltd.</span>
    </div>
  </section>

  <section class="card card-back" aria-label="Card back">
    <div class="back-panel"></div>
    <h1 class="holder-name">MARK <strong>TELFORD</strong></h1>
    <p class="holder-title">Architectural Designer &amp; Design RQC</p>

    <div class="contact-box">
      <ul class="contact-list">
        <li class="contact-item">02 5319 6620
          <svg class="contact-icon" viewBox="0 0 28 28" aria-hidden="true">
            <circle cx="14" cy="14" r="14" fill="#fff"/>
            <rect x="10" y="6.5" width="8" height="15" rx="1.5" fill="none" stroke="#3d3d3f" stroke-width="1.6"/>
            <circle cx="14" cy="18.6" r="0.9" fill="#3d3d3f"/>
          </svg>
        </li>
        <li class="contact-item">www.kdstudio.co.nz
          <svg class="contact-icon" viewBox="0 0 28 28" aria-hidden="true">
            <circle cx="14" cy="14" r="14" fill="#fff"/>
            <circle cx="14" cy="14" r="8" fill="none" stroke="#3d3d3f" stroke-width="1.6"/>
            <ellipse cx="14" cy="14" rx="3.5" ry="8" fill="none" stroke="#3d3d3f" stroke-width="1.4"/>
            <line x1="6" y1="14" x2="22" y2="14" stroke="#3d3d3f" stroke-width="1.4"/>
          </svg>
        </li>
        <li class="contact-item">mark@kdstudio.co.nz
          <svg class="contact-icon" viewBox="0 0 28 28" aria-hidden="true">
            <circle cx="14" cy="14" r="14" fill="#fff"/>
            <rect x="7" y="9" width="14" height="10" rx="1" fill="#3d3d3f"/>
            <polyline points="7.5,9.5 14,15 20.5,9.5" fill="none" stroke="#fff" stroke-width="1.3"/>
          </svg>
        </li>
      </ul>
    </div>

    <div class="badge-seal" role="img" aria-label="Licensed practitioner badge"></div>
    <div class="badge-member" role="img" aria-label="Professional membership badge"></div>
  </section>
</main>
</body>
</html>
```